Harbor Crest Mortgages

We would like to revamp our business cards to make them look more sleek and professional. please provide some with barcode and some without, and use the proper logo (attached). Would like the color #5ac689 to be a little more predominant, and use the WOODFORD BOURNE MEDIUM font, per the attached brand guidelines. Would like end product for Tobias and for Dean (see attached).
Industry/Entity Type
Finance
Contact Information for Business Card
see sample provided, email, tel# etc.
Requirements
Must have
- could some of the designs also include the bar code please? just some...

```html
<!DOCTYPE html>
<html lang="en">
<head>
<meta charset="utf-8">
<title>Harbor Crest Mortgages – Business Cards</title>
<link rel="stylesheet" href="https://fonts.googleapis.com/css2?family=Mulish:wght@400;600;700;800&family=Montserrat:wght@400;500&display=swap">
<style>
  :root {
    --charcoal: #2b2a29;
    --brand-green: #5ac689;
    --black: #111111;
    --white: #ffffff;
    --page: #ffffff;
  }
  * { box-sizing: border-box; margin: 0; padding: 0; }
  html, body { width: 1200px; height: 559px; overflow: hidden; background: var(--page); }
  .sheet { position: relative; width: 1200px; height: 559px; font-family: "Mulish", sans-serif; }

  .card { position: absolute; width: 272px; height: 152px; background: var(--bg); color: var(--ink); overflow: hidden; }
  .theme-dark { --bg: var(--charcoal); --ink: var(--brand-green); --pattern: rgba(90,198,137,0.28); }
  .theme-green-black { --bg: var(--brand-green); --ink: var(--black); --pattern: rgba(40,120,80,0.35); }
  .theme-green-white { --bg: var(--brand-green); --ink: var(--white); --pattern: rgba(255,255,255,0.28); }

  .col-1 { left: 32px; } .col-2 { left: 320px; } .col-3 { left: 610px; } .col-4 { left: 898px; }
  .row-1 { top: 34px; } .row-2 { top: 204px; } .row-3 { top: 373px; }

  /* Front lockup */
  .front .brand-mark { position: absolute; left: 52px; top: 58px; width: 32px; height: 32px; background: var(--ink); }
  .front .divider { position: absolute; left: 101px; top: 46px; width: 1px; height: 60px; background: var(--ink); }
  .front .brand-name { position: absolute; left: 109px; top: 52px; font-weight: 800; font-size: 15px; line-height: 16px; color: var(--ink); text-transform: uppercase; letter-spacing: 0.3px; }
  .front .membership { position: absolute; left: 109px; top: 92px; font-family: "Montserrat", sans-serif; font-size: 4.8px; line-height: 5.8px; color: var(--ink); }
  .front .partner-badge { position: absolute; left: 174px; top: 90px; width: 55px; height: 11px; border: 1px solid var(--ink); }
  .front .partner-badge::before { content: ""; position: absolute; left: 0; top: 0; width: 18px; height: 9px; background: var(--ink); }

  /* Back */
  .back .pattern { position: absolute; right: 0; top: 0; width: 110px; height: 152px; background: linear-gradient(to right, transparent, var(--pattern)); }
  .back .brand-mark { position: absolute; left: 22px; top: 18px; width: 20px; height: 20px; background: var(--ink); }
  .back .divider { position: absolute; left: 50px; top: 15px; width: 0.6px; height: 31px; background: var(--ink); }
  .back .brand-name { position: absolute; left: 54px; top: 18px; font-weight: 800; font-size: 7px; line-height: 8px; text-transform: uppercase; color: var(--ink); }
  .back .membership { position: absolute; left: 54px; top: 38px; font-family: "Montserrat", sans-serif; font-size: 2.2px; line-height: 2.7px; }
  .back .partner-badge { position: absolute; left: 86px; top: 38px; width: 27px; height: 5.5px; border: 0.6px solid var(--ink); }
  .back .partner-badge::before { content: ""; position: absolute; left: 0; top: 0; width: 9px; height: 4.3px; background: var(--ink); }

  .person-name { position: absolute; font-weight: 800; font-size: 11px; letter-spacing: 0.4px; text-transform: uppercase; white-space: nowrap; }
  .person-role { position: absolute; font-weight: 400; font-size: 6px; letter-spacing: 0.3px; white-space: nowrap; }
  .phone { position: absolute; display: flex; align-items: center; gap: 7px; font-weight: 600; font-size: 11px; letter-spacing: 0.3px; white-space: nowrap; }
  .contact { position: absolute; display: flex; align-items: center; gap: 7px; font-size: 7px; font-weight: 600; letter-spacing: 0.2px; white-space: nowrap; }
  .icon { width: 8px; height: 8px; fill: none; stroke: var(--ink); stroke-width: 1.2; }
  .icon.solid { fill: var(--ink); stroke: none; }

  .dean .person-name { left: 90px; top: 64px; }
  .dean .person-role { left: 90px; top: 77px; }
  .dean .phone { left: 94px; top: 110px; }
  .dean .email { left: 31px; top: 129px; }
  .dean .web { left: 146px; top: 130px; }

  .tobias .person-name { left: 71px; top: 70px; }
  .tobias .person-role { left: 71px; top: 83px; }
  .tobias .phone { left: 89px; top: 110px; }
  .tobias .email { left: 30px; top: 129px; }
  .tobias .web { left: 146px; top: 130px; }
</style>
</head>
<body>
<main class="sheet">

  <!-- Row 1 -->
  <section class="card front theme-dark row-1 col-1">
    <span class="brand-mark"></span><span class="divider"></span>
    <p class="brand-name">Harbor Crest<br>Mortgages</p>
    <p class="membership">Independently owned &amp;<br>operated member of</p>
    <span class="partner-badge"></span>
  </section>
  <section class="card back dean theme-dark row-1 col-2">
    <div class="pattern" role="img" aria-label="Faint repeating brand pattern along the right edge"></div>
    <span class="brand-mark"></span><span class="divider"></span>
    <p class="brand-name">Harbor Crest<br>Mortgages</p>
    <p class="membership">Independently owned &amp;<br>operated member of</p>
    <span class="partner-badge"></span>
    <p class="person-name">Dean Whitlock</p>
    <p class="person-role">Broker Owner</p>
    <p class="phone"><svg class="icon solid" viewBox="0 0 24 24"><path d="M6.6 10.8a15 15 0 0 0 6.6 6.6l2.2-2.2c.3-.3.7-.4 1-.2 1.1.4 2.3.6 3.6.6.6 0 1 .4 1 1V20c0 .6-.4 1-1 1A17 17 0 0 1 3 4c0-.6.4-1 1-1h3.5c.6 0 1 .4 1 1 0 1.3.2 2.5.6 3.6.1.3 0 .7-.2 1z"/></svg>416-555-0173</p>
    <p class="contact email"><svg class="icon" viewBox="0 0 24 24"><rect x="2" y="5" width="20" height="14"/><path d="M2 5l10 8 10-8"/></svg>Dean@HarborCrest.ca</p>
    <p class="contact web"><svg class="icon" viewBox="0 0 24 24"><rect x="4" y="4" width="16" height="12"/><path d="M1 20h22"/></svg>www.DeanWhitlock.com</p>
  </section>
  <section class="card front theme-dark row-1 col-3">
    <span class="brand-mark"></span><span class="divider"></span>
    <p class="brand-name">Harbor Crest<br>Mortgages</p>
    <p class="membership">Independently owned &amp;<br>operated member of</p>
    <span class="partner-badge"></span>
  </section>
  <section class="card back tobias theme-dark row-1 col-4">
    <div class="pattern" role="img" aria-label="Faint repeating brand pattern along the right edge"></div>
    <span class="brand-mark"></span><span class="divider"></span>
    <p class="brand-name">Harbor Crest<br>Mortgages</p>
    <p class="membership">Independently owned &amp;<br>operated member of</p>
    <span class="partner-badge"></span>
    <p class="person-name">Tobias Renner</p>
    <p class="person-role">Broker Owner</p>
    <p class="phone"><svg class="icon solid" viewBox="0 0 24 24"><path d="M6.6 10.8a15 15 0 0 0 6.6 6.6l2.2-2.2c.3-.3.7-.4 1-.2 1.1.4 2.3.6 3.6.6.6 0 1 .4 1 1V20c0 .6-.4 1-1 1A17 17 0 0 1 3 4c0-.6.4-1 1-1h3.5c.6 0 1 .4 1 1 0 1.3.2 2.5.6 3.6.1.3 0 .7-.2 1z"/></svg>416-555-0173</p>
    <p class="contact email"><svg class="icon" viewBox="0 0 24 24"><rect x="2" y="5" width="20" height="14"/><path d="M2 5l10 8 10-8"/></svg>Dean@HarborCrest.ca</p>
    <p class="contact web"><svg class="icon" viewBox="0 0 24 24"><rect x="4" y="4" width="16" height="12"/><path d="M1 20h22"/></svg>www.DeanWhitlock.com</p>
  </section>

  <!-- Row 2 -->
  <section class="card front theme-green-black row-2 col-1">
    <span class="brand-mark"></span><span class="divider"></span>
    <p class="brand-name">Harbor Crest<br>Mortgages</p>
    <p class="membership">Independently owned &amp;<br>operated member of</p>
    <span class="partner-badge"></span>
  </section>
  <section class="card back dean theme-green-black row-2 col-2">
    <div class="pattern" role="img" aria-label="Faint repeating brand pattern along the right edge"></div>
    <span class="brand-mark"></span><span class="divider"></span>
    <p class="brand-name">Harbor Crest<br>Mortgages</p>
    <p class="membership">Independently owned &amp;<br>operated member of</p>
    <span class="partner-badge"></span>
    <p class="person-name">Dean Whitlock</p>
    <p class="person-role">Broker Owner</p>
    <p class="phone"><svg class="icon solid" viewBox="0 0 24 24"><path d="M6.6 10.8a15 15 0 0 0 6.6 6.6l2.2-2.2c.3-.3.7-.4 1-.2 1.1.4 2.3.6 3.6.6.6 0 1 .4 1 1V20c0 .6-.4 1-1 1A17 17 0 0 1 3 4c0-.6.4-1 1-1h3.5c.6 0 1 .4 1 1 0 1.3.2 2.5.6 3.6.1.3 0 .7-.2 1z"/></svg>416-555-0173</p>
    <p class="contact email"><svg class="icon" viewBox="0 0 24 24"><rect x="2" y="5" width="20" height="14"/><path d="M2 5l10 8 10-8"/></svg>Dean@HarborCrest.ca</p>
    <p class="contact web"><svg class="icon" viewBox="0 0 24 24"><rect x="4" y="4" width="16" height="12"/><path d="M1 20h22"/></svg>www.DeanWhitlock.com</p>
  </section>
  <section class="card front theme-green-black row-2 col-3">
    <span class="brand-mark"></span><span class="divider"></span>
    <p class="brand-name">Harbor Crest<br>Mortgages</p>
    <p class="membership">Independently owned &amp;<br>operated member of</p>
    <span class="partner-badge"></span>
  </section>
  <section class="card back tobias theme-green-black row-2 col-4">
    <div class="pattern" role="img" aria-label="Faint repeating brand pattern along the right edge"></div>
    <span class="brand-mark"></span><span class="divider"></span>
    <p class="brand-name">Harbor Crest<br>Mortgages</p>
    <p class="membership">Independently owned &amp;<br>operated member of</p>
    <span class="partner-badge"></span>
    <p class="person-name">Tobias Renner</p>
    <p class="person-role">Broker Owner</p>
    <p class="phone"><svg class="icon solid" viewBox="0 0 24 24"><path d="M6.6 10.8a15 15 0 0 0 6.6 6.6l2.2-2.2c.3-.3.7-.4 1-.2 1.1.4 2.3.6 3.6.6.6 0 1 .4 1 1V20c0 .6-.4 1-1 1A17 17 0 0 1 3 4c0-.6.4-1 1-1h3.5c.6 0 1 .4 1 1 0 1.3.2 2.5.6 3.6.1.3 0 .7-.2 1z"/></svg>416-555-0173</p>
    <p class="contact email"><svg class="icon" viewBox="0 0 24 24"><rect x="2" y="5" width="20" height="14"/><path d="M2 5l10 8 10-8"/></svg>Dean@HarborCrest.ca</p>
    <p class="contact web"><svg class="icon" viewBox="0 0 24 24"><rect x="4" y="4" width="16" height="12"/><path d="M1 20h22"/></svg>www.DeanWhitlock.com</p>
  </section>

  <!-- Row 3 -->
  <section class="card front theme-green-white row-3 col-1">
    <span class="brand-mark"></span><span class="divider"></span>
    <p class="brand-name">Harbor Crest<br>Mortgages</p>
    <p class="membership">Independently owned &amp;<br>operated member of</p>
    <span class="partner-badge"></span>
  </section>
  <section class="card back dean theme-green-white row-3 col-2">
    <div class="pattern" role="img" aria-label="Faint repeating brand pattern along the right edge"></div>
    <span class="brand-mark"></span><span class="divider"></span>
    <p class="brand-name">Harbor Crest<br>Mortgages</p>
    <p class="membership">Independently owned &amp;<br>operated member of</p>
    <span class="partner-badge"></span>
    <p class="person-name">Dean Whitlock</p>
    <p class="person-role">Broker Owner</p>
    <p class="phone"><svg class="icon solid" viewBox="0 0 24 24"><path d="M6.6 10.8a15 15 0 0 0 6.6 6.6l2.2-2.2c.3-.3.7-.4 1-.2 1.1.4 2.3.6 3.6.6.6 0 1 .4 1 1V20c0 .6-.4 1-1 1A17 17 0 0 1 3 4c0-.6.4-1 1-1h3.5c.6 0 1 .4 1 1 0 1.3.2 2.5.6 3.6.1.3 0 .7-.2 1z"/></svg>416-555-0173</p>
    <p class="contact email"><svg class="icon" viewBox="0 0 24 24"><rect x="2" y="5" width="20" height="14"/><path d="M2 5l10 8 10-8"/></svg>Dean@HarborCrest.ca</p>
    <p class="contact web"><svg class="icon" viewBox="0 0 24 24"><rect x="4" y="4" width="16" height="12"/><path d="M1 20h22"/></svg>www.DeanWhitlock.com</p>
  </section>
  <section class="card front theme-green-white row-3 col-3">
    <span class="brand-mark"></span><span class="divider"></span>
    <p class="brand-name">Harbor Crest<br>Mortgages</p>
    <p class="membership">Independently owned &amp;<br>operated member of</p>
    <span class="partner-badge"></span>
  </section>
  <section class="card back tobias theme-green-white row-3 col-4">
    <div class="pattern" role="img" aria-label="Faint repeating brand pattern along the right edge"></div>
    <span class="brand-mark"></span><span class="divider"></span>
    <p class="brand-name">Harbor Crest<br>Mortgages</p>
    <p class="membership">Independently owned &amp;<br>operated member of</p>
    <span class="partner-badge"></span>
    <p class="person-name">Tobias Renner</p>
    <p class="person-role">Broker Owner</p>
    <p class="phone"><svg class="icon solid" viewBox="0 0 24 24"><path d="M6.6 10.8a15 15 0 0 0 6.6 6.6l2.2-2.2c.3-.3.7-.4 1-.2 1.1.4 2.3.6 3.6.6.6 0 1 .4 1 1V20c0 .6-.4 1-1 1A17 17 0 0 1 3 4c0-.6.4-1 1-1h3.5c.6 0 1 .4 1 1 0 1.3.2 2.5.6 3.6.1.3 0 .7-.2 1z"/></svg>416-555-0173</p>
    <p class="contact email"><svg class="icon" viewBox="0 0 24 24"><rect x="2" y="5" width="20" height="14"/><path d="M2 5l10 8 10-8"/></svg>Dean@HarborCrest.ca</p>
    <p class="contact web"><svg class="icon" viewBox="0 0 24 24"><rect x="4" y="4" width="16" height="12"/><path d="M1 20h22"/></svg>www.DeanWhitlock.com</p>
  </section>

</main>
</body>
</html>
```